Looking for a5 flyer for domestic properties in Scotland
One side on Air Source Heat pumps (air to water Heat pump) Instalation + maintenance
Other side Air to Air Heat Pumps also knows as Air Conditioning Heat Pumps. Installation
Design to be Black white with red blue
Halloran- Climacore Services

Need sell the benifts of large energy savings over oil and lpg and lowering carbon footprint

```html
<!DOCTYPE html>
<html lang="en">
<head>
<meta charset="utf-8">
<title>Halloran – Climacore Services Heat Pump Flyer</title>
<link href="https://fonts.googleapis.com/css2?family=Archivo+Black&family=Roboto+Condensed:wght@300;400;700&display=swap" rel="stylesheet">
<style>
  :root{
    --black:#000;
    --charcoal:#231f20;
    --blue:#26a8e0;
    --orange:#f15a29;
    --white:#fff;
    --grey:#8a8a8a;
    --band:rgba(125,62,38,.88);
    --page:#e4e4e4;
  }
  *{margin:0;padding:0;box-sizing:border-box}
  html,body{width:1200px;height:1200px;overflow:hidden;background:var(--page)}
  body{position:relative;font-family:"Roboto Condensed",sans-serif;color:var(--white)}
  .flyer{position:absolute;width:566px;height:804px;overflow:hidden;background:var(--black)}
  .flyer--front{left:24px;top:36px}
  .flyer--back{left:613px;top:370px}
  .abs{position:absolute;white-space:nowrap}
  .headline{font-family:"Archivo Black",sans-serif;font-size:54px;line-height:46px;letter-spacing:-1px}
  .blue{color:var(--blue)}
  .orange{color:var(--orange)}
  .audience{font-size:27px;font-weight:400}
  .audience b{font-weight:700}
  .services-line{font-size:33px;font-weight:700}
  .services-line .plus{color:var(--white);font-size:28px}
  .benefits{font-size:21px;font-weight:700;color:var(--grey);line-height:26px}
  .product-visual{position:absolute;left:0;top:336px;width:566px;height:240px;
    background:linear-gradient(180deg,#3a3c3e 0%,#2b2d2e 100%)}
  .service-photo{position:absolute;left:0;top:0;width:566px;height:578px;
    background:linear-gradient(160deg,#2a2a2a 0%,#1c1c1c 50%,#2e2f31 75%,#161616 100%)}
  .footer{position:absolute;left:0;top:578px;width:566px;height:226px;background:var(--charcoal)}
  .footer .bar-blue{position:absolute;left:530px;top:2px;width:36px;height:116px;background:var(--blue)}
  .footer .bar-orange{position:absolute;left:530px;top:118px;width:36px;height:108px;background:var(--orange)}
  .brand{left:62px;top:24px;font-size:80px;font-weight:700;letter-spacing:-3px;line-height:72px}
  .tagline{left:62px;top:104px;font-size:23px;font-weight:700;letter-spacing:-.3px}
  .phone{left:60px;top:134px;font-size:58px;font-weight:700;color:var(--orange);line-height:60px}
  .web{left:60px;top:198px;font-size:20px;font-weight:700;color:var(--blue)}
  .band{position:absolute;height:38px;background:var(--band)}
  .band-label{font-size:24px;font-weight:400;line-height:38px}
  .band-label b{font-weight:700}
  .body-copy{font-size:25px;font-weight:300;line-height:32px;letter-spacing:.3px}
</style>
</head>
<body>

<section class="flyer flyer--front">
  <div class="abs headline blue" style="left:64px;top:48px">AIR SOURCE</div>
  <div class="abs headline orange" style="left:64px;top:94px">HEAT PUMPS</div>
  <div class="abs audience" style="left:66px;top:160px">AIR TO WATER <b>FOR SCOTTISH HOMES</b></div>
  <div class="abs services-line" style="left:64px;top:214px"><span class="blue">INSTALLATION</span> <span class="plus">+</span> <span class="orange">MAINTENANCE</span></div>
  <div class="abs benefits" style="left:64px;top:268px">LARGE ENERGY SAVINGS OVER OIL &amp; LPG HEATING<br>&amp; A LOWER CARBON FOOTPRINT FOR YOUR HOME</div>
  <div class="product-visual" role="img" aria-label="Outdoor air source heat pump unit mounted beside a house wall"></div>
  <div class="footer">
    <div class="bar-blue"></div><div class="bar-orange"></div>
    <div class="abs brand">Halloran</div>
    <div class="abs tagline">Climacore Services for your home.</div>
    <div class="abs phone">0800 555 0192</div>
    <div class="abs web">WWW.HALLORAN.COOL</div>
  </div>
</section>

<section class="flyer flyer--back">
  <div class="service-photo" role="img" aria-label="Engineer fitting an indoor air to air heat pump unit in a living room"></div>
  <div class="abs headline blue" style="left:58px;top:68px">AIR TO AIR</div>
  <div class="abs headline orange" style="left:58px;top:114px">HEAT PUMPS</div>
  <div class="band" style="left:0;top:176px;width:330px"></div>
  <div class="abs band-label" style="left:60px;top:176px">ALSO KNOWN AS <b>AIR CON</b></div>
  <div class="abs body-copy" style="left:60px;top:228px">Air Conditioning Heat Pumps that<br>heat in winter and cool in summer,<br>with large savings over oil and LPG</div>
  <div class="band" style="left:190px;top:342px;width:376px"></div>
  <div class="abs band-label" style="left:204px;top:342px">LOWER <b>CARBON</b></div>
  <div class="abs body-copy" style="left:204px;top:394px">Cut your home's carbon<br>footprint with efficient<br>electric heating</div>
  <div class="abs services-line" style="left:62px;top:514px"><span class="blue">INSTALLATION</span> <span class="plus">+</span> <span class="orange">ACROSS SCOTLAND</span></div>
  <div class="footer">
    <div class="bar-blue"></div><div class="bar-orange"></div>
    <div class="abs brand">Halloran</div>
    <div class="abs tagline">Climacore Services for your home.</div>
    <div class="abs phone">0800 555 0192</div>
    <div class="abs web">WWW.HALLORAN.COOL</div>
  </div>
</section>

</body>
</html>
```